Real Estate Site Update - wordpress

my wordpress site has not been updated in 6 years and needs a makeover
1. I would like to include my new logo (attached)
2. I would also like to include new staff photos (attached)
3. I would like to include client video testimonials (attached)
4. I would like to have real estate agent bio template pages for current and new agents
5. the site needs mobile device functionality
6. I would like a new look and more overall usability and functionality
Pages needed
1. main page
2. about us page
3. agent bio page template
4. 1st time buyer class sign up page - handbook purchase (coinvale)
5. property search pages (lotfinder hub)
6. first time buyer picture and announcement blog page
7. buyer information resources
8. seller information resources
I am looking for interesting Ideas on how to make my real estate website POP
current page is brightkeyhaven.com
I currently have and need
1. ability to post to social media (Activated)
2. I'd like to incorporate my youtube page brightkeyhavenny
3. ability to register clients for class attendance (activated need presentation update)
4. ability to charge for class and booklets via coinvale (activated)
5. ability to provide mls listing searches via lotfinderhub activated needs better presentation
if access to my current website file structure will assist please advise, i will gladly provide access
wordpress tools currently activated
QTRV
Pour Along
Lockmoat
Tablekit
Snipo
Lotfinder Hub
ages 22-50 income 30k and up
Real Estate

```html
<!DOCTYPE html>
<html lang="en">
<head>
<meta charset="utf-8">
<title>Brightkey Haven – Home</title>
<link href="https://fonts.googleapis.com/css2?family=Roboto:wght@300;400;500;700&display=swap" rel="stylesheet">
<style>
:root{
  --navy:#2a3340;
  --navy-dark:#1e2630;
  --pink:#e0506e;
  --ink:#222;
  --muted:#666;
  --line:#d6d6d6;
  --white:#fff;
  --grey:#cfcfcf;
}
*{box-sizing:border-box;margin:0;padding:0}
html,body{width:811px;height:1200px;overflow:hidden;background:#fff;font-family:"Roboto",Arial,sans-serif;color:var(--ink)}
.page{position:relative;width:811px;height:1200px;overflow:hidden}
.abs{position:absolute}

/* header */
.header{left:0;top:0;width:811px;height:63px;background:linear-gradient(#2c3542,#353f4d)}
.topline{left:165px;top:7px;width:481px;display:flex;justify-content:space-between;font-size:6px;color:#cfd5dd}
.topline .right{display:flex;gap:6px;align-items:center}
.soc{width:9px;height:9px;border-radius:50%;background:#5a6574;display:inline-block}
.logo{left:165px;top:26px;color:#fff;font-size:9px;font-weight:500;letter-spacing:1px;display:flex;align-items:center;gap:4px}
.logo .dot{width:8px;height:8px;background:var(--pink);border-radius:50%}
.nav{left:315px;top:46px;display:flex;align-items:center;font-size:6.5px;color:#dde2e8}
.nav a{padding:0 7px;color:inherit;text-decoration:none}
.nav .active{background:var(--pink);color:#fff;padding:5px 12px;font-weight:500;margin-right:6px}
.phone{left:564px;top:47px;background:var(--pink);color:#fff;font-size:8.5px;font-weight:500;padding:3px 6px;display:flex;align-items:center;gap:5px}

/* hero */
.hero{left:0;top:63px;width:811px;height:249px;background:linear-gradient(100deg,#1d6fc4 0%,#4b95db 35%,#b9a688 60%,#d9c9a2 80%,#8a6b45 100%)}
.dots{right:38px;top:288px;display:flex;gap:4px}
.dots i{width:7px;height:7px;border-radius:50%;background:#fff}
.dots i:first-child{background:var(--pink)}

/* search */
.search{left:165px;top:304px;width:481px;height:84px;background:#fff;border:1px solid #ccc;padding:14px 16px}
.field{position:absolute;font-size:6px;color:#666}
.field .box{margin-top:5px;height:11px;border:1px solid #ccc;font-size:5.5px;color:#888;padding:2px 4px;position:relative}
.field .box.sel:after{content:"";position:absolute;right:0;top:0;width:11px;height:9px;border-left:1px solid #ccc}
.range{position:absolute;height:3px;background:var(--pink)}
.range:before,.range:after{content:"";position:absolute;top:-3px;width:7px;height:7px;border-radius:50%;background:#fff;border:1px solid #bbb}
.range:before{left:-3px}.range:after{right:-3px}
.searchbtn{left:401px;top:51px;width:64px;height:16px;background:var(--navy-dark);color:#fff;font-size:6.5px;font-weight:500;display:flex;align-items:center;justify-content:center}

/* featured */
.tag{left:165px;top:401px;width:82px;height:17px;background:var(--pink);color:#fff;font-size:6.5px;font-weight:500;display:flex;align-items:center;gap:5px;padding-left:6px}
.tag i{width:6px;height:6px;background:#fff;opacity:.8}
.arrows{left:628px;top:405px;display:flex;gap:2px}
.arrows i{width:8px;height:8px;background:#8a8f96}
.card{width:111px;height:135px;border:1px solid #ddd;background:#fff}
.card .img{height:74px}
.g1{background:linear-gradient(#6d8fae,#3e4a3a 60%,#3f6b2c)}
.g2{background:linear-gradient(#9ab3cd,#7b7d7d 55%,#4e7f36)}
.g3{background:linear-gradient(#cfe0ee,#8c7f76 55%,#6f8d55)}
.card h4{font-size:6.3px;font-weight:500;margin:7px 0 0 8px}
.card .loc{font-size:5px;font-style:italic;margin:4px 0 0 10px;color:#333}
.card .price{margin:4px 0 0 9px;display:flex;height:10px;width:58px;font-size:6px;color:#fff;font-weight:500}
.card .price b{width:14px;background:#111;display:flex;align-items:center;justify-content:center}
.card .price span{flex:1;background:var(--navy-dark);display:flex;align-items:center;justify-content:center;margin-left:1px}
.stats{display:flex;margin-top:3px;border-top:1px solid #ddd}
.stats div{flex:1;font-size:4.8px;text-align:center;padding-top:2px;height:16px;border-right:1px solid #ddd;line-height:1.15}
.stats div:last-child{border:0}

/* lower three columns */
.col h3{font-size:10px;font-weight:500;margin-bottom:8px}
.feat{display:flex;gap:6px;margin-bottom:13px}
.feat svg{flex:none}
.feat b{display:block;font-size:6px;font-weight:500}
.feat p{font-size:5px;color:#555;line-height:1.25;width:130px}
.agentimg{width:152px;height:91px;border:1px solid #ccc;background:linear-gradient(135deg,#d8dce0,#f3f1ec 50%,#b9c6d6)}
.agentrow{display:flex;justify-content:space-between;margin-top:8px;font-size:6px}
.morebtn{margin-top:4px;background:var(--navy-dark);color:#fff;font-size:4px;padding:2px 8px;display:inline-block}
.testibox{width:148px;height:88px;border:1px solid #ccc;padding:6px 8px;font-size:4.8px;line-height:1.3;color:#444;text-align:justify}
.avatar{width:26px;height:26px;border-radius:50%;background:linear-gradient(#cfd3d8,#6d7480);border:2px solid #eee}

/* partners + footer */
.darkband{left:0;top:910px;width:811px;height:186px;background:var(--navy-dark)}
.partners{left:165px;top:910px;width:380px;height:47px;background:#fff;display:flex;align-items:center;gap:28px;padding-left:26px}
.badge{width:44px;height:18px;background:#c9d3de;border-radius:3px}
.ourpartners{left:515px;top:903px;width:131px;height:63px}
.ourpartners span{position:absolute;left:44px;top:18px;color:#fff;font-size:10px;text-align:center;line-height:1.2}
.fcol h3{color:#fff;font-size:10.5px;font-weight:500;margin-bottom:9px}
.fcol li{list-style:none;font-size:6px;color:#e8ecf0;margin-bottom:6.6px}
.inp{width:115px;height:13px;background:#fff;font-size:5.5px;color:#999;padding:3px 6px;margin-bottom:6px}
.news{left:0;top:1096px;width:811px;height:85px;background:var(--pink)}
.news h5{position:absolute;left:311px;top:27px;color:#fff;font-size:7.5px;font-weight:400;letter-spacing:.3px}
.news .nin{position:absolute;left:311px;top:40px;width:145px;height:16px;background:#fff}
.news .nbtn{position:absolute;left:457px;top:40px;width:43px;height:16px;background:#c73d5b;color:#fff;font-size:7.5px;display:flex;align-items:center;justify-content:center}
.bottom{left:0;top:1181px;width:811px;height:19px;background:#c9c9c9;font-size:4.8px;color:#333;display:flex;align-items:center;justify-content:space-between;padding:0 165px}
.bottom .links{display:flex;gap:20px}
</style>
</head>
<body>
<div class="page">

<header class="abs header"></header>
<div class="abs topline"><span>Email us at: info@brightkeyhaven.com</span>
  <span class="right">Login &nbsp;|&nbsp; Register
    <i class="soc" aria-label="social link"></i><i class="soc" aria-label="social link"></i><i class="soc" aria-label="social link"></i><i class="soc" aria-label="social link"></i><i class="soc" aria-label="social link"></i></span></div>
<div class="abs logo"><i class="dot"></i>BRIGHTKEY HAVEN</div>
<nav class="abs nav"><a class="active">Home</a><a>Listing</a><a>News</a><a>IDX</a><a>Gallery</a><a>Pages</a><a>Contact us</a></nav>
<div class="abs phone">
  <svg width="6" height="6" viewBox="0 0 10 10"><path d="M2 1l2 2-1 1.5c.8 1.4 1.6 2.2 3 3L7.5 6.5l2 2L8 10C4 9.5.5 6 0 2z" fill="#fff"/></svg>
  1-000-555-0142</div>

<div class="abs hero" role="img" aria-label="Hand holding a house key in front of a villa"></div>
<div class="abs dots"><i></i><i></i><i></i><i></i></div>

<section class="abs search">
  <div class="field" style="left:16px;top:14px;width:57px">Property ID<div class="box">Any</div></div>
  <div class="field" style="left:81px;top:14px;width:154px">Property Location<div class="box sel">Any</div></div>
  <div class="field" style="left:243px;top:14px;width:105px">Property Status<div class="box sel">Any</div></div>
  <div class="field" style="left:358px;top:14px;width:106px">Property Type<div class="box sel">Any</div></div>
  <div class="field" style="left:16px;top:44px;width:57px">Min Beds<div class="box sel">Any</div></div>
  <div class="field" style="left:81px;top:44px;width:57px">Min Baths<div class="box sel">Any</div></div>
  <div class="field" style="left:148px;top:44px;width:118px">Price<span style="float:right">$10.000 - $20.000</span></div>
  <div class="range" style="left:151px;top:61px;width:113px"></div>
  <div class="field" style="left:274px;top:44px;width:118px">Price<span style="float:right">$10.000 - $20.000</span></div>
  <div class="range" style="left:277px;top:61px;width:113px"></div>
  <div class="abs searchbtn">Search</div>
</section>

<div class="abs tag"><i></i>Festured Properties</div>
<div class="abs arrows"><i></i><i></i></div>

<!-- property cards -->
<div class="abs card" style="left:165px;top:431px"><div class="img g1" role="img" aria-label="Modern house at dusk"></div><h4>116 Wavely lace (rs-1707)</h4><div class="loc">⌖ California</div><div class="price"><b>$</b><span>10000</span></div><div class="stats"><div>5000<br>AREA</div><div>3<br>BATHS</div><div>4<br>BEDS</div><div>2<br>PARKSING</div></div></div>
<div class="abs card" style="left:289px;top:431px"><div class="img g2" role="img" aria-label="Grey family house with lawn"></div><h4>116 Wavely lace (rs-1707)</h4><div class="loc">⌖ California</div><div class="price"><b>$</b><span>10000</span></div><div class="stats"><div>5000<br>AREA</div><div>3<br>BATHS</div><div>4<br>BEDS</div><div>2<br>PARKSING</div></div></div>
<div class="abs card" style="left:412px;top:431px"><div class="img g3" role="img" aria-label="Two-storey beach house"></div><h4>116 Wavely lace (rs-1707)</h4><div class="loc">⌖ California</div><div class="price"><b>$</b><span>10000</span></div><div class="stats"><div>5000<br>AREA</div><div>3<br>BATHS</div><div>4<br>BEDS</div><div>2<br>PARKSING</div></div></div>
<div class="abs card" style="left:536px;top:431px"><div class="img g1" role="img" aria-label="Modern house at dusk"></div><h4>116 Wavely lace (rs-1707)</h4><div class="loc">⌖ California</div><div class="price"><b>$</b><span>10000</span></div><div class="stats"><div>5000<br>AREA</div><div>3<br>BATHS</div><div>4<br>BEDS</div><div>2<br>PARKSING</div></div></div>

<div class="abs card" style="left:165px;top:579px"><div class="img g1" role="img" aria-label="Modern house at dusk"></div><h4>116 Wavely lace (rs-1707)</h4><div class="loc">⌖ California</div><div class="price"><b>$</b><span>10000</span></div><div class="stats"><div>5000<br>AREA</div><div>3<br>BATHS</div><div>4<br>BEDS</div><div>2<br>PARKSING</div></div></div>
<div class="abs card" style="left:289px;top:579px"><div class="img g2" role="img" aria-label="Grey family house with lawn"></div><h4>116 Wavely lace (rs-1707)</h4><div class="loc">⌖ California</div><div class="price"><b>$</b><span>10000</span></div><div class="stats"><div>5000<br>AREA</div><div>3<br>BATHS</div><div>4<br>BEDS</div><div>2<br>PARKSING</div></div></div>
<div class="abs card" style="left:412px;top:579px"><div class="img g3" role="img" aria-label="Two-storey beach house"></div><h4>116 Wavely lace (rs-1707)</h4><div class="loc">⌖ California</div><div class="price"><b>$</b><span>10000</span></div><div class="stats"><div>5000<br>AREA</div><div>3<br>BATHS</div><div>4<br>BEDS</div><div>2<br>PARKSING</div></div></div>
<div class="abs card" style="left:536px;top:579px"><div class="img g1" role="img" aria-label="Modern house at dusk"></div><h4>116 Wavely lace (rs-1707)</h4><div class="loc">⌖ California</div><div class="price"><b>$</b><span>10000</span></div><div class="stats"><div>5000<br>AREA</div><div>3<br>BATHS</div><div>4<br>BEDS</div><div>2<br>PARKSING</div></div></div>

<!-- theme features -->
<section class="abs col" style="left:165px;top:728px;width:150px">
  <h3>Theme Features</h3>
  <div class="feat"><svg width="12" height="12" viewBox="0 0 12 12"><path d="M0 6a6 5 0 0 1 12 0zM6 6v4a1 1 0 0 1-2 0" fill="none" stroke="#2a3340" stroke-width="1.4"/><path d="M0 6a6 5 0 0 1 12 0z" fill="#2a3340"/></svg><div><b>Lots of possibilities</b><p>Lorem ipsum dolor sit amet, consectetur adipiscing elit.</p></div></div>
  <div class="feat"><svg width="12" height="12" viewBox="0 0 12 12" fill="#2a3340"><rect y="1" width="3" height="2"/><rect x="4" y="1" width="8" height="2"/><rect y="5" width="3" height="2"/><rect x="4" y="5" width="8" height="2"/><rect y="9" width="3" height="2"/><rect x="4" y="9" width="8" height="2"/></svg><div><b>Property list view</b><p>Lorem ipsum dolor sit amet, consectetur adipiscing elit.</p></div></div>
  <div class="feat"><svg width="12" height="12" viewBox="0 0 12 12"><circle cx="5" cy="5" r="3.6" fill="none" stroke="#2a3340" stroke-width="1.6"/><path d="M7.5 7.5l3.5 3.5" stroke="#2a3340" stroke-width="2"/></svg><div><b>Advance Search Options</b><p>Lorem ipsum dolor sit amet, consectetur adipiscing elit.</p></div></div>
  <div class="feat"><svg width="12" height="12" viewBox="0 0 12 12" fill="#2a3340"><circle cx="6" cy="3.5" r="2.3"/><path d="M1.5 11a4.5 4 0 0 1 9 0z"/><circle cx="2" cy="4.5" r="1.5"/><circle cx="10" cy="4.5" r="1.5"/></svg><div><b>Agents Profile</b><p>Lorem ipsum dolor sit amet, consectetur adipiscing elit.</p></div></div>
</section>

<!-- popular agent -->
<section class="abs col" style="left:329px;top:728px;width:152px">
  <h3>Popular Agent</h3>
  <div class="agentimg" role="img" aria-label="Smiling agent at her office desk"></div>
  <div class="agentrow">
    <div>Lena Marsh<br><span class="morebtn">More Details</span></div>
    <div style="font-size:5px;line-height:1.6">✆ 1-000-555-0142<br>✉ info@brightkeyhaven.com</div>
  </div>
</section>

<!-- testimonials -->
<section class="abs col" style="left:493px;top:728px;width:153px">
  <h3>Client Testimonials</h3>
  <div class="testibox">Lorem Ipsum is simply dummy text of the printing and typesetting industry. Lorem Ipsum has been the industry's standard dummy text ever since the 1500s, when .<br>Lorem Ipsum is simply dummy text of the printing and typesetting industry. Lorem Ipsum has been the industry's standard dummy text ever since the 1500s, when .<br>Lorem Ipsum is simply dummy text of the printing and typesetting industry. Lorem Ipsum has been the industry's standard dummy text ever since the 1500s, when .</div>
  <div style="display:flex;justify-content:space-between;margin-top:8px">
    <div style="font-size:5px;font-weight:500;line-height:1.6">Carla Dunn - Dunn Studio<br>www.carladunn.net</div>
    <div class="avatar" role="img" aria-label="Client portrait"></div>
  </div>
  <div style="position:absolute;left:65px;top:141px;display:flex;gap:3px"><i style="width:7px;height:7px;border-radius:50%;background:var(--pink)"></i><i style="width:7px;height:7px;border-radius:50%;background:#1e2630"></i></div>
</section>

<!-- partners -->
<div class="abs darkband"></div>
<div class="abs partners">
  <i class="badge" aria-label="partner"></i><i class="badge" aria-label="partner"></i><i class="badge" aria-label="partner"></i><i class="badge" aria-label="partner"></i><i class="badge" aria-label="partner"></i>
</div>
<div class="abs ourpartners"><svg width="131" height="63"><polygon points="30,0 131,0 101,63 0,63" fill="#e0506e"/></svg><span>Our<br>Partners</span></div>

<!-- footer -->
<div class="abs fcol" style="left:165px;top:989px"><h3>Quick Links</h3><ul><li>Home</li><li>Listing</li><li>News</li><li>IDX</li><li>Gallery</li><li>Pages</li></ul></div>
<div class="abs fcol" style="left:288px;top:989px"><h3>About Us</h3><ul><li>Compnay Info</li><li>Gallery</li><li>Agents</li></ul></div>
<div class="abs fcol" style="left:412px;top:989px"><h3>Contact Us</h3><ul><li>ADDRESS:</li><li>----------------------------------</li><li>----------------------------------</li><li>Phone: 1-000-555-0142</li><li>Email: info@brightkeyhaven.com</li></ul></div>
<div class="abs fcol" style="left:536px;top:989px"><h3>Blog Updates Signup</h3><div class="inp">User Name</div><div class="inp">Password</div></div>

<section class="abs news"><h5>JOIN OUR NEWSLETTER</h5><div class="nin"></div><div class="nbtn">SIGN UP</div></section>
<footer class="abs bottom"><span>Copyright © 2016 Brightkey Haven. Use of this website constitutes acceptance of our User Agreement and Privacy Policy.</span><span class="links"><span>Terms</span><span>Privacy</span><span>Security</span></span></footer>

</div>
</body>
</html>
```